Dental practice Re-design and relaunch the website while retaining the CI

We need a re-desgin of our totally obsolete and poorly maintained page (it was problematic to make changes). The wish is that we get a contemporary design and above all the site can update itself without much know-how about web techniques have to have. The current website: www.praxis-karlwehr.de Pictures are then made available and made available.

Target Market(s)

patient information

Number of Pages Required

1 page

Font styles to use
Sans Serif

Colors

Designer to choose colors to be used in the design.

Requirements
Must have
• An area that we can revitalize ourselves with little effort!
Should not have
• Animations or similar

```html
<!DOCTYPE html>
<html lang="de">
<head>
<meta charset="utf-8">
<title>Praxis Karlwehr</title>
<link rel="stylesheet" href="https://fonts.googleapis.com/css2?family=Roboto:wght@400;500;700&family=Open+Sans:wght@400;600&display=swap">
<style>
:root{
  --ink:#1d1d1d;
  --band:#222222;
  --text:#3a3a3a;
  --muted:#6d6d6d;
  --line:#cfcfcf;
  --white:#ffffff;
  --icon:#555555;
}
*{margin:0;padding:0;box-sizing:border-box}
html,body{width:1200px;height:2314px;overflow:hidden;background:var(--white)}
body{position:relative;font-family:"Open Sans",Arial,sans-serif;color:var(--text)}
.abs{position:absolute}
.topbar{left:0;top:0;width:1200px;height:42px;background:var(--ink);color:var(--white);font-family:"Roboto",Arial,sans-serif;font-size:15px;font-weight:500}
.topbar span{position:absolute;top:12px}
.navbar{left:0;top:42px;width:1200px;height:51px;background:var(--white);border-bottom:1px solid #e6e6e6}
.navbar a{position:absolute;top:17px;font-family:"Roboto",Arial,sans-serif;font-size:13.5px;font-weight:500;color:var(--ink);text-decoration:none;letter-spacing:.3px}
.brand{left:99px;top:0;width:191px;height:93px;background:var(--white);display:flex;flex-direction:column;align-items:center;justify-content:center;font-family:"Roboto",Arial,sans-serif;font-weight:400;color:var(--ink);padding-top:12px}
.brand small{font-size:10.5px;letter-spacing:.5px}
.brand strong{font-weight:400;font-size:20px;letter-spacing:1px}
.hero{left:0;top:93px;width:1200px;height:481px;background:linear-gradient(100deg,#6f5a4e 0%,#a89384 35%,#8a7d78 60%,#4e4640 100%)}
.hero-copy{left:0;top:270px;width:1200px;text-align:center;color:var(--white);font-family:"Roboto",Arial,sans-serif}
.hero-copy h2{font-size:30px;font-weight:500;margin-bottom:22px}
.hero-copy h1{font-size:34px;font-weight:700}
.btn-appoint{left:398px;top:398px;width:414px;height:59px;border:2px solid var(--white);color:var(--white);font-family:"Roboto",Arial,sans-serif;font-size:28px;font-weight:500;display:flex;align-items:center;justify-content:center}
.feature{top:604px;width:240px;text-align:center}
.feature .ring{width:70px;height:70px;border:3px solid #c9c9c9;border-radius:50%;margin:0 auto;display:flex;align-items:center;justify-content:center}
.feature h3{font-family:"Roboto",Arial,sans-serif;font-weight:400;font-size:18px;color:var(--ink);margin:24px 0 14px}
.feature p{font-size:12px;line-height:19.5px;color:var(--muted)}
.meetband{left:0;top:844px;width:1200px;height:105px;background:var(--band);color:var(--white);font-family:"Roboto",Arial,sans-serif}
.meetband h3{position:absolute;left:98px;top:24px;font-size:23px;font-weight:400}
.meetband p{position:absolute;left:98px;top:58px;font-size:19px}
.btn-check{position:absolute;left:848px;top:32px;width:253px;height:40px;border:2px solid var(--white);display:flex;align-items:center;justify-content:center;gap:8px;font-size:16px;font-weight:500}
.welcome{left:100px;top:998px;width:1000px;text-align:center}
.welcome h2{font-family:"Roboto",Arial,sans-serif;font-size:24px;font-weight:700;color:var(--ink)}
.welcome .lead{font-size:14px;color:var(--ink);margin-top:16px}
.welcome .body{font-size:11.8px;line-height:23px;color:var(--muted);margin-top:20px}
.video{top:1214px;width:466px;height:334px;color:var(--white);font-family:"Roboto",Arial,sans-serif;font-weight:700;font-size:24px;text-align:center;line-height:36px;letter-spacing:.3px}
.video .caption{position:absolute;left:0;width:100%;top:150px}
.video svg{display:block;margin:0 auto 16px}
.doctors{left:120px;background:linear-gradient(180deg,#a9abab 0%,#8f9495 55%,#77797a 100%)}
.elders{left:616px;background:linear-gradient(180deg,#6e6e6e 0%,#5d5d5d 70%,#4e4e4e 100%)}
.testi-title{left:0;top:1595px;width:1200px;text-align:center;font-family:"Roboto",Arial,sans-serif;font-size:29px;font-weight:700;color:var(--ink)}
.card{top:1674px;width:462px;height:221px;border:1px solid var(--line);background:var(--white)}
.photo{top:1690px;width:199px;height:190px}
.card h4{position:absolute;top:54px;font-family:"Montserrat","Roboto",Arial,sans-serif;font-size:18px;font-weight:500;color:var(--ink)}
.card p{position:absolute;top:92px;width:260px;font-size:12px;line-height:21px;color:var(--muted);text-align:justify}
.map{left:0;top:1941px;width:1200px;height:327px;background:linear-gradient(135deg,#e4e4e4 0%,#d8d8d8 50%,#e2e2e2 100%)}
.contact{left:383px;top:2003px;width:439px;height:208px;background:rgba(40,40,40,.88);color:var(--white);padding:30px 0 0 30px;font-family:"Montserrat","Roboto",Arial,sans-serif;font-size:15.5px;font-weight:500}
.contact li{list-style:none;display:flex;align-items:center;gap:16px;height:41px}
.contact svg{flex:none}
.footer{left:0;top:2268px;width:1200px;height:46px;background:var(--ink);color:var(--white);font-family:"Montserrat","Roboto",Arial,sans-serif;font-size:12px;text-align:center;line-height:46px}
</style>
</head>
<body>

<header>
  <div class="abs topbar">
    <span style="left:561px">Reach Us @&nbsp; +49 711 55 20 418</span>
    <span style="left:808px">Live chat @&nbsp; info@praxis-karlwehr.de</span>
  </div>
  <nav class="abs navbar">
    <a style="left:469px">PHILOSOPHIE</a>
    <a style="left:640px">PRAXIS</a>
    <a style="left:767px">KONTAKT</a>
    <a style="left:911px">ANFAHRT</a>
    <a style="left:1056px">LINKS</a>
  </nav>
  <div class="abs brand"><small>ZAHNÄRZTLICHE PRAXIS</small><strong>KARLWEHR</strong></div>
</header>

<section class="abs hero" role="img" aria-label="Photo of a smiling young man and woman at the dentist"></section>
<div class="abs hero-copy">
  <h2>In Order To Give You</h2>
  <h1>AN UNTROUBLED LAUGH AGAIN, LET'S GIVE IT TO US</h1>
</div>
<div class="abs btn-appoint">MAKE AN APPOINTMENT</div>

<section>
  <div class="abs feature" style="left:86px">
    <div class="ring"><svg width="36" height="36" viewBox="0 0 36 36" fill="none" stroke="var(--icon)" stroke-width="2.6" stroke-linecap="round"><path d="M8 4v9a7 7 0 0 0 14 0V4"/><path d="M15 20v5a6 6 0 0 0 12 0v-5"/><circle cx="27" cy="16" r="3.5"/></svg></div>
    <h3>Trusted</h3>
    <p>Lorem Ipsum is simply dummy text of the printing and typesetting industry. Lorem Ipsum has been the industry's standard dummy text 1500s.</p>
  </div>
  <div class="abs feature" style="left:349px">
    <div class="ring"><svg width="34" height="34" viewBox="0 0 34 34"><path d="M10 15v-4a7 7 0 0 1 14 0v4" fill="none" stroke="var(--icon)" stroke-width="3"/><rect x="7" y="15" width="20" height="15" rx="2" fill="var(--icon)"/></svg></div>
    <h3>Security</h3>
    <p>Lorem Ipsum is simply dummy text of the printing and typesetting industry. Lorem Ipsum has been the industry's standard dummy text 1500s.</p>
  </div>
  <div class="abs feature" style="left:617px">
    <div class="ring"><svg width="36" height="36" viewBox="0 0 36 36" fill="none" stroke="var(--icon)" stroke-width="2.4"><rect x="5" y="10" width="26" height="20" rx="2"/><path d="M13 10V6h10v4"/><path d="M18 14v12M12 20h12"/></svg></div>
    <h3>Cost Effective</h3>
    <p>Lorem Ipsum is simply dummy text of the printing and typesetting industry. Lorem Ipsum has been the industry's standard dummy text 1500s.</p>
  </div>
  <div class="abs feature" style="left:876px">
    <div class="ring"><svg width="36" height="36" viewBox="0 0 36 36" fill="none" stroke="var(--icon)" stroke-width="2.4"><circle cx="18" cy="12" r="6.5"/><path d="M6 32c0-7 5-11 12-11s12 4 12 11"/><path d="M18 22v6M15 25h6"/></svg></div>
    <h3>Qualified Doctors</h3>
    <p>Lorem Ipsum is simply dummy text of the printing and typesetting industry. Lorem Ipsum has been the industry's standard dummy text 1500s.</p>
  </div>
</section>

<section class="abs meetband">
  <h3>Now It Makes Easier To Meet Our Doctors</h3>
  <p>check it out how to reach us quickly.</p>
  <div class="btn-check">CHECK IT OUT HERE <svg width="20" height="12" viewBox="0 0 20 12"><path d="M0 6h17M12 1l6 5-6 5" fill="none" stroke="#fff" stroke-width="2"/></svg></div>
</section>

<section class="abs welcome">
  <h2>WELCOME TO PRAXIS-KARLWEHR</h2>
  <p class="lead">We will do our best to give you an untroubled laugh</p>
  <p class="body">For most people, a dentist's visit is unpleasant! Why? You are simply afraid because in your past was this visit Regularly associated with pain. Imagine you go to the dentist and he has not drilled at all! The is truly not a utopia, but rather a vision that through certain Precautionary measures can become reality for every human being! Have we made you a little curious? Nice ... then you invest just a few minutes of your precious time, and we'll show you the way ... with it. Our practice is strongly geared towards dental health care. These preventive measures begin with the elucidation of an expectant mother And practically never stop. In detailed oral hygiene instructions.</p>
</section>

<section>
  <div class="abs video doctors" role="img" aria-label="Photo of a dentist with arms crossed in a treatment room">
    <div class="caption">
      <svg width="30" height="30" viewBox="0 0 30 30"><circle cx="15" cy="15" r="13" fill="none" stroke="#fff" stroke-width="3"/><path d="M12 9l9 6-9 6z" fill="#fff"/></svg>
      CHECK OUT WHAT OUR DOCTORS<br>SAYS ABOUT YOUR TEETH
    </div>
  </div>
  <div class="abs video elders" role="img" aria-label="Photo of two cheerful elderly men raising walking sticks">
    <div class="caption">
      <svg width="30" height="30" viewBox="0 0 30 30"><circle cx="15" cy="15" r="13" fill="none" stroke="#fff" stroke-width="3"/><path d="M12 9l9 6-9 6z" fill="#fff"/></svg>
      AGE &amp; CONDITION OF YOUR TEETH<br>IS DOEN'T MATTER
    </div>
  </div>
</section>

<h2 class="abs testi-title">TESTIMONIALS</h2>
<section>
  <div class="abs card" style="left:122px">
    <h4 style="left:193px">K Morland</h4>
    <p style="left:193px">"Lorem Ipsum is simply dummy text of the printing and typesetting industry. Lorem Ipsum has been the industry's standard dummy text ever since the 1500s,"</p>
  </div>
  <div class="abs photo" style="left:100px;background:linear-gradient(160deg,#d9d9d9,#8a8a8a)" role="img" aria-label="Portrait of a smiling man in glasses and bow tie"></div>
  <div class="abs card" style="left:603px">
    <h4 style="left:182px">Mrs Hale</h4>
    <p style="left:17px;text-align:justify">"Lorem Ipsum is simply dummy text of the printing and typesetting industry. Lorem Ipsum has been the industry's standard dummy text ever since the 1500s,"</p>
  </div>
  <div class="abs photo" style="left:903px;background:linear-gradient(160deg,#6c5a50,#3f6d95)" role="img" aria-label="Portrait of a smiling young man in a blue shirt"></div>
</section>

<section class="abs map" role="img" aria-label="Street map around the practice location"></section>
<ul class="abs contact">
  <li><svg width="20" height="18" viewBox="0 0 20 18"><path d="M10 1L1 9h3v8h4v-5h4v5h4V9h3z" fill="#fff"/></svg>Lindenhofweg 12, 70439 Stuttgart</li>
  <li><svg width="18" height="18" viewBox="0 0 18 18"><rect width="18" height="18" rx="3" fill="#fff"/><path d="M5 4l2 0 1 3-1.5 1a7 7 0 0 0 3.5 3.5L11 10l3 1v2a1 1 0 0 1-1 1A10 10 0 0 1 4 5a1 1 0 0 1 1-1z" fill="#333"/></svg>+49 711 55 20 418</li>
  <li><svg width="20" height="14" viewBox="0 0 20 14"><rect width="20" height="14" fill="#fff"/><path d="M0 0l10 8 10-8" fill="none" stroke="#333" stroke-width="1.6"/></svg>info@praxis-karlwehr.de</li>
  <li><svg width="18" height="18" viewBox="0 0 18 18"><circle cx="9" cy="9" r="8" fill="#fff"/><path d="M9 4v5h4" fill="none" stroke="#333" stroke-width="1.8"/></svg>Mon - Thur: 8am - 6pm;&nbsp; Fri - Sat: 8am - 1pm</li>
</ul>

<footer class="abs footer">© Copyright 2017 - Praxis-Karlwehr All Rights Reserved &nbsp;| Privacy Policy | Terms &amp; Conditions</footer>

</body>
</html>
```